Re-design of website: www.veltramedia.ca/en/

Veltrameda B is a promotional agency specializing in on-site marketing. We are re-designing their website.

We have already produced a prototype:
http://norvapixel.com/veltramedia_siteweb/

The architecture in the prototype must be respected. Please dress up the design with green, grey and black circles and other textures found on their current website www.veltramedia.ca

Inspiration for design that we like, clean, flat design:

- http://www.brimfoxlab.co/
- http://quellarworks.com/#!/process
- http://wearetolvane.com/

Delivrables: PSD files of each page of the prototype

Here are the images of their print portfolio: http://ftp.veltramedia.ca/clients/VLM/VELTRAMEDIA-PORTFOLIO-2012_EN.zip

Industry/Entity Type

Architecture

Requirements
Must have
• Responsive Design

```html
<!DOCTYPE html>
<html lang="fr">
<head>
<meta charset="utf-8">
<title>Veltrameda B</title>
<link href="https://fonts.googleapis.com/css2?family=PT+Sans:wght@400;700&display=swap" rel="stylesheet">
<style>
:root{
  --green:#7cc242;
  --green-dark:#5ea82a;
  --green-light:#9ad45f;
  --ink:#2b2b2b;
  --dark-disc:#333333;
  --grey-text:#6b6b6b;
  --grey-line:#e2e2e2;
  --soft-bg:#f4f4f4;
  --white:#ffffff;
}
*{margin:0;padding:0;box-sizing:border-box}
html,body{width:812px;height:1200px;overflow:hidden;background:var(--white)}
body{font-family:"PT Sans",sans-serif;color:var(--ink);position:relative}
.top-strip{position:absolute;left:0;top:0;width:812px;height:4px;background:#ececec}
.lang-select{position:absolute;left:689px;top:4px;width:69px;height:22px;background:#efefef;font-size:11px;color:#444;display:flex;align-items:center;justify-content:center;gap:5px}
.lang-select svg{width:8px;height:5px}
.brand{position:absolute;left:0;width:812px;top:28px;height:36px;display:flex;align-items:center;justify-content:center;gap:10px}
.brand-name{font-size:30px;font-weight:700;letter-spacing:3px;color:var(--ink);text-transform:uppercase}
.brand-dot{width:30px;height:30px;border-radius:50%;background:var(--green)}
.main-nav{position:absolute;left:0;top:87px;width:812px;height:41px;background:linear-gradient(#9bd35d,#6fb935);}
.nav-item{position:absolute;top:12px;font-size:13px;color:var(--white);letter-spacing:.2px}
.nav-sep{position:absolute;top:14px;width:1px;height:14px;background:rgba(255,255,255,.55)}
.social{position:absolute;top:10px;width:20px;height:20px;border-radius:50%;background:#eef6e4}
.hero{position:absolute;left:0;top:128px;width:812px;height:282px;background:linear-gradient(90deg,#d7b79b 0%,#caa080 30%,#e6d7c8 55%,#b9d6cc 75%,#dfe8ea 100%)}
.hero-caption{position:absolute;left:419px;top:144px;width:339px;height:100px;background:rgba(255,255,255,.85);padding:16px 0 0 21px}
.hero-title{font-size:22px;font-weight:700;line-height:24px;color:var(--ink)}
.hero-sub{font-size:18px;line-height:22px;color:var(--ink)}
.hero-text{font-size:10px;margin-top:4px;color:#444}
.hero-arrows{position:absolute;left:51px;top:250px;width:24px;height:14px}
.section-title{position:absolute;left:0;width:812px;top:428px;text-align:center;font-size:23px;color:var(--green-dark)}
.work{position:absolute;width:349px;height:181px;overflow:hidden}
.work-visual{position:absolute;inset:0}
.work-band{position:absolute;left:0;bottom:0;width:349px;height:40px}
.work-label{position:absolute;left:15px;bottom:8px;font-size:13px;color:var(--ink)}
.services{position:absolute;left:0;top:884px;width:812px;height:270px;background:linear-gradient(var(--white),var(--soft-bg));border-top:1px solid var(--grey-line)}
.service{position:absolute;top:20px;width:200px;margin-left:-100px;text-align:center}
.service-disc{width:172px;height:172px;border-radius:50%;background:var(--dark-disc);margin:0 auto;position:relative}
.service-disc svg{position:absolute;left:56px;top:36px;width:60px;height:56px}
.service-name{position:absolute;left:0;width:172px;top:100px;font-size:19px;color:var(--green)}
.service-text{font-size:10px;line-height:14px;color:var(--grey-text);margin-top:13px}
.site-footer{position:absolute;left:0;top:1154px;width:812px;height:46px;border-top:1px solid var(--grey-line);background:var(--white)}
.site-footer p{position:absolute;left:51px;top:18px;font-size:9.5px;color:#777}
</style>
</head>
<body>
<div class="top-strip"></div>
<div class="lang-select">English <svg viewBox="0 0 8 5"><path d="M0 0h8L4 5z" fill="#555"/></svg></div>

<header class="brand">
  <span class="brand-name">Veltrameda B</span>
  <span class="brand-dot"></span>
</header>

<nav class="main-nav">
  <span class="nav-item" style="left:78px">AGENCE</span>
  <span class="nav-sep" style="left:141px"></span>
  <span class="nav-item" style="left:157px">SERVICES</span>
  <span class="nav-sep" style="left:225px"></span>
  <span class="nav-item" style="left:241px">REALISATIONS</span>
  <span class="nav-sep" style="left:339px"></span>
  <span class="nav-item" style="left:355px">EVENEMENTS</span>
  <span class="nav-sep" style="left:447px"></span>
  <span class="nav-item" style="left:463px">RECRUTEMENT</span>
  <span class="nav-sep" style="left:564px"></span>
  <span class="nav-item" style="left:579px">CONTACT</span>
  <span class="social" style="left:668px"></span>
  <span class="social" style="left:691px"></span>
  <span class="social" style="left:714px"></span>
  <span class="social" style="left:737px"></span>
</nav>

<section class="hero" role="img" aria-label="Photo of a smiling young woman outdoors by the water">
  <div class="hero-caption">
    <h1 class="hero-title">VIVERRA VESTIBULUM SUSPEND</h1>
    <p class="hero-sub">DUIS TINCIDUNT LECTUS</p>
    <p class="hero-text">Nunc tempus felis vitae urna Vivamus porttitor g purus</p>
  </div>
  <svg class="hero-arrows" viewBox="0 0 24 14"><path d="M8 1L2 7l6 6M16 1l6 6-6 6" fill="none" stroke="#222" stroke-width="1.6"/></svg>
</section>

<h2 class="section-title">Nos réalisations 360</h2>

<article class="work" style="left:48px;top:469px">
  <div class="work-visual" role="img" aria-label="Illustration of white kitchen utensils on yellow-green stripes" style="background:linear-gradient(90deg,#e3e92a,#d0e02a)"></div>
  <svg class="work-band" viewBox="0 0 349 40" preserveAspectRatio="none"><path d="M0 0L349 18V40H0z" fill="var(--green)"/></svg>
  <span class="work-label">Nunc tempus felis vitae urna</span>
</article>
<article class="work" style="left:415px;top:469px">
  <div class="work-visual" role="img" aria-label="Promotional photo of a winter event in snowy mountains" style="background:linear-gradient(#6b9ed2,#dde8f2 70%,#f3f6f8)"></div>
  <svg class="work-band" viewBox="0 0 349 40" preserveAspectRatio="none"><path d="M0 0L349 18V40H0z" fill="var(--green)"/></svg>
  <span class="work-label">Aliquam nec erat at purus cursus</span>
</article>
<article class="work" style="left:48px;top:659px">
  <div class="work-visual" role="img" aria-label="Promotional photo of three event hostesses against a mountain backdrop" style="background:linear-gradient(#b8cde0,#8fa9c4 60%,#c8d5df)"></div>
  <svg class="work-band" viewBox="0 0 349 40" preserveAspectRatio="none"><path d="M0 0L349 18V40H0z" fill="var(--green)"/></svg>
  <span class="work-label">Duis tincidunt lectus quis dui</span>
</article>
<article class="work" style="left:415px;top:659px">
  <div class="work-visual" role="img" aria-label="Product photo of a bottle splashing in green liquid" style="background:radial-gradient(circle at 50% 45%,#e3a23a 0,#c98a22 22%,#7cc242 48%,#4f9a24 100%)"></div>
  <svg class="work-band" viewBox="0 0 349 40" preserveAspectRatio="none"><path d="M0 0L349 18V40H0z" fill="var(--green)"/></svg>
  <span class="work-label">Ut ac mi quis lacus mollis</span>
</article>

<section class="services">
  <div class="service" style="left:153px">
    <div class="service-disc">
      <svg viewBox="0 0 60 56"><path d="M12 8c4-3 7-2 8 1l3 8c1 3-1 5-3 6l-2 1c2 6 6 11 11 14l2-2c2-2 4-2 6 0l6 5c2 2 2 5-1 7-4 4-10 5-16 0C16 40 9 30 8 20c-1-5 1-9 4-12z" fill="#fff"/><path d="M34 14c4 2 6 6 6 10M38 6c6 3 10 10 10 18" fill="none" stroke="#fff" stroke-width="3" stroke-linecap="round"/></svg>
      <span class="service-name">Contact</span>
    </div>
    <p class="service-text">Lorem ipsum dolor sit amet, consect-<br>etuer adipiscing elit. Nam cursus. Morbi<br>ut mi. Nullam enim leo egestas</p>
  </div>
  <div class="service" style="left:406px">
    <div class="service-disc">
      <svg viewBox="0 0 60 56"><circle cx="30" cy="14" r="9" fill="#fff"/><circle cx="12" cy="20" r="6" fill="#fff"/><circle cx="48" cy="20" r="6" fill="#fff"/><path d="M14 46c0-12 7-19 16-19s16 7 16 19z" fill="#fff"/><path d="M0 40c0-8 5-12 12-12 2 0 3 0 4 1-3 3-4 7-4 11zM60 40c0-8-5-12-12-12-2 0-3 0-4 1 3 3 4 7 4 11z" fill="#fff"/></svg>
      <span class="service-name">Recruitment</span>
    </div>
    <p class="service-text">Lorem ipsum dolor sit amet, consect-<br>etuer adipiscing elit. Nam cursus. Morbi<br>ut mi. Nullam enim leo egestas</p>
  </div>
  <div class="service" style="left:661px">
    <div class="service-disc">
      <svg viewBox="0 0 60 56"><ellipse cx="26" cy="14" rx="9" ry="11" fill="#fff"/><path d="M8 52c0-14 6-22 18-22 6 0 10 2 13 5v17z" fill="#fff"/><path d="M41 34h6v7h7v6h-7v7h-6v-7h-7v-6h7z" fill="#fff" stroke="var(--dark-disc)" stroke-width="2"/></svg>
      <span class="service-name">Follow Us</span>
    </div>
    <p class="service-text">Lorem ipsum dolor sit amet, consect-<br>etuer adipiscing elit. Nam cursus. Morbi<br>ut mi. Nullam enim leo egestas</p>
  </div>
</section>

<footer class="site-footer">
  <p>© 2013 Company Name.&nbsp; All right reserved.&nbsp; Term of Use</p>
</footer>
</body>
</html>
```